Tribe as pace "La tribu marca el paso"

I'm writing a book about word of mouth and the consumer as the media "the book is in Spanish" so you have to use "La tribu marca el paso" the subtitle is and 30 examples that proves it "Más 30 relatos de la plaza"

Book is about the power of consumer nowadays , the book will combine the era of social media but also the power of one to one word of mouth meaning w/o being connected to an electronic platform

Tribe sets the pace is a book about the power that now the consumer has in this double way interaction between the brands and the consumer, between the services and the people between the social media and the traditional media.

Consumer is on control and it is because "tribe sets the pace"

About book principles
I love simple books white background, simplicity around the fonts and the images (simple is better)

Target Market(s)

Marketing and digital marketing managers, social media managers, community managers, social media agencies, business people

Industry/Entity Type

Electronic

Requirements
Must have
• White backgroung, black and red fonts big fonts
Nice to have
• the subtitle "Más 30 relatos de la calle"

```html
<!DOCTYPE html>
<html lang="es">
<head>
<meta charset="utf-8">
<title>La tribu marca el paso — cubierta</title>
<link rel="stylesheet" href="https://fonts.googleapis.com/css2?family=Archivo+Black&family=Roboto+Condensed:wght@700&display=swap">
<style>
  :root {
    --stage: #2b2b2b;
    --paper: #f4f4f4;
    --paper-edge: #e2e2e2;
    --ink: #141414;
    --accent: #d9191c;
    --icon-grey: #b4b4b4;
    --hand-grey: #8f8f8f;
    --label-text: #ffffff;
  }
  html, body {
    margin: 0;
    padding: 0;
    width: 1200px;
    height: 1031px;
    overflow: hidden;
    background: var(--stage);
  }
  .book-cover {
    position: absolute;
    left: 280px;
    top: 35px;
    width: 640px;
    height: 960px;
    background: linear-gradient(180deg, #ffffff 0%, var(--paper) 100%);
    box-shadow: inset -3px 0 0 var(--paper-edge);
    overflow: hidden;
  }
  .icon-field {
    position: absolute;
    left: 24px;
    top: 24px;
    width: 592px;
    height: 340px;
    background: linear-gradient(180deg, rgba(150,150,150,0.45) 0%, rgba(180,180,180,0.3) 60%, rgba(255,255,255,0) 100%);
  }
  .title-block {
    position: absolute;
    left: 60px;
    top: 385px;
    width: 520px;
  }
  .title {
    margin: 0;
    font-family: "Archivo Black", "Arial Black", sans-serif;
    font-weight: 400;
    line-height: 1;
  }
  .title__line {
    display: block;
    white-space: nowrap;
  }
  .title__lead {
    color: var(--accent);
    font-size: 60px;
    letter-spacing: -1px;
  }
  .title__second {
    text-align: right;
    margin-top: -4px;
  }
  .title__small {
    color: var(--accent);
    font-size: 60px;
    letter-spacing: -1px;
    margin-right: 12px;
  }
  .title__big {
    color: var(--ink);
    font-size: 128px;
    letter-spacing: -3px;
  }
  .subtitle {
    margin: 4px 0 0;
    text-align: right;
    font-family: "Roboto Condensed", "Arial Narrow", sans-serif;
    font-weight: 700;
    font-size: 22px;
    color: var(--ink);
  }
  .hands-art {
    position: absolute;
    left: 130px;
    top: 700px;
    width: 320px;
    height: 260px;
    background: linear-gradient(180deg, rgba(170,170,170,0.25) 0%, rgba(150,150,150,0.7) 55%, var(--hand-grey) 100%);
  }
  .author-label {
    position: absolute;
    left: 470px;
    top: 790px;
    width: 170px;
    height: 34px;
    background: var(--ink);
    color: var(--label-text);
    font-family: "Archivo Black", "Arial Black", sans-serif;
    font-size: 15px;
    line-height: 34px;
    padding-left: 14px;
    box-sizing: border-box;
    letter-spacing: 1px;
  }
</style>
</head>
<body>
  <main class="book-cover">
    <div class="icon-field" role="img" aria-label="Patrón gris de iconos de redes, mensajes y dispositivos"></div>

    <div class="title-block">
      <h1 class="title">
        <span class="title__line title__lead">La tribu marca</span>
        <span class="title__line title__second"><span class="title__small">el</span><span class="title__big">paso</span></span>
      </h1>
      <p class="subtitle">Más 30 relatos de la plaza</p>
    </div>

    <div class="hands-art" role="img" aria-label="Ilustración en grises de manos alzadas"></div>

    <div class="author-label">AUTHOR NAME</div>
  </main>
</body>
</html>
```